Banner Ad for Weight Loss Product Site

We need a banner ad design for a new company selling a weight loss online programme (Ebook). The product is called "Your FitRoute" and is suitable for people that want to lose weight fast and without doing sports, regardless of age. We would like to see designs that are eye-catching and at its best animated like in the example files. The final design should exhibit a professional look that encourages the customers to buy our product. The text should be "Persönlicher Diätplan zum Abnehmen?" as a title and "Jetzt informieren" for the button field. Thank you!

```html
<!DOCTYPE html>
<html lang="de">
<head>
<meta charset="utf-8">
<title>Your FitRoute – Banner</title>
<link href="https://fonts.googleapis.com/css2?family=Oswald:wght@600;700&family=Open+Sans:wght@700;800&display=swap" rel="stylesheet">
<style>
  :root {
    --page-bg: #ececec;
    --page-line: #e3e3e3;
    --caption: #707070;
    --green: #6cb21f;
    --green-dark: #4f8f12;
    --green-light: #a6d44a;
    --lime-top: #d9ea4f;
    --orange: #f6a41c;
    --orange-dark: #e0780a;
    --white: #ffffff;
    --btn-text: #2a1a05;
  }
  * { margin: 0; padding: 0; box-sizing: border-box; }
  html, body { width: 1200px; height: 721px; overflow: hidden; }
  body {
    background: var(--page-bg);
    background-image: repeating-linear-gradient(45deg, var(--page-line) 0 2px, transparent 2px 8px);
    position: relative;
    font-family: "Open Sans", sans-serif;
  }
  .banner {
    position: absolute;
    left: 296px; top: 44px;
    width: 609px; height: 500px;
    overflow: hidden;
    background: var(--white);
  }
  .banner-top, .banner-bottom { position: absolute; left: 0; top: 0; }
  .model-photo {
    position: absolute;
    left: 378px; top: 0;
    width: 231px; height: 430px;
    background: linear-gradient(180deg, #7a4a32 0%, #c89478 40%, #d9a98c 62%, #2b2b2b 88%);
    border-radius: 90px 0 0 0;
  }
  .headline {
    position: absolute;
    left: 27px; top: 38px;
    font-family: "Oswald", sans-serif;
    font-weight: 700;
    font-size: 48px;
    line-height: 63px;
    color: var(--green);
    text-transform: uppercase;
    letter-spacing: 0.3px;
    white-space: nowrap;
  }
  .product-photo {
    position: absolute;
    left: 30px; top: 246px;
    width: 149px; height: 123px;
    background: linear-gradient(135deg, #f4f4f4 0%, #d9d9d9 50%, #8fb84a 100%);
    border-radius: 4px;
  }
  .pointer-arrow { position: absolute; left: 266px; top: 237px; }
  .brand {
    position: absolute;
    left: 18px; top: 374px;
    width: 110px; height: 110px;
    border-radius: 50%;
    background: var(--green-light);
    border: 3px solid var(--lime-top);
    display: flex; align-items: center; justify-content: center;
  }
  .brand-name {
    font-family: "Open Sans", sans-serif;
    font-weight: 800;
    font-size: 17px;
    line-height: 20px;
    color: var(--white);
    text-align: center;
  }
  .cta {
    position: absolute;
    left: 206px; top: 424px;
    width: 332px; height: 56px;
    border-radius: 28px;
    background: linear-gradient(180deg, #ffd24a 0%, var(--orange) 55%, var(--orange-dark) 100%);
    display: flex; align-items: center;
    padding-left: 24px;
    font-family: "Open Sans", sans-serif;
    font-weight: 800;
    font-size: 25px;
    color: var(--btn-text);
    white-space: nowrap;
    box-shadow: 0 2px 3px rgba(0,0,0,0.25);
  }
  .cta-icon {
    position: absolute;
    right: 10px; top: 10px;
    width: 36px; height: 36px;
  }
  .caption {
    position: absolute;
    left: 0; top: 573px;
    width: 1200px;
    text-align: center;
    font-family: "Open Sans", sans-serif;
    font-weight: 800;
    font-size: 51px;
    line-height: 58px;
    color: var(--caption);
    text-transform: uppercase;
    white-space: nowrap;
  }
</style>
</head>
<body>
  <div class="banner">
    <svg class="banner-top" width="609" height="80" viewBox="0 0 609 80">
      <path d="M0 0 H609 V26 Q330 64 0 34 Z" fill="var(--green)"/>
      <path d="M0 34 Q330 64 609 26 V40 Q330 78 0 46 Z" fill="var(--lime-top)"/>
    </svg>
    <div class="model-photo" role="img" aria-label="Fotografie: lächelnde Frau in Sportkleidung zeigt nach vorn und misst ihre Taille mit einem Maßband"></div>
    <svg class="banner-bottom" width="609" height="500" viewBox="0 0 609 500">
      <path d="M0 382 Q300 360 609 372 V500 H0 Z" fill="var(--orange)"/>
      <path d="M0 394 Q300 374 609 386 V500 H0 Z" fill="var(--green)"/>
      <path d="M0 462 Q300 444 609 452 V500 H0 Z" fill="var(--green-dark)"/>
    </svg>
    <div class="product-photo" role="img" aria-label="Produktabbildung: Ratgeber-Ebook mit CD"></div>
    <h1 class="headline">Persönlicher<br>Diätplan zum<br>Abnehmen?</h1>
    <svg class="pointer-arrow" width="36" height="103" viewBox="0 0 36 103">
      <path d="M12 4 Q4 40 18 92" stroke="var(--green)" stroke-width="4" fill="none" stroke-linecap="round"/>
      <path d="M5 74 L18 94 L31 70" stroke="var(--green)" stroke-width="4" fill="none" stroke-linecap="round" stroke-linejoin="round"/>
    </svg>
    <div class="brand"><span class="brand-name">Your<br>FitRoute</span></div>
    <div class="cta">Jetzt informieren
      <svg class="cta-icon" viewBox="0 0 36 36">
        <circle cx="18" cy="18" r="17" fill="#fbd96a"/>
        <path d="M14 11 L21 18 L14 25" stroke="var(--btn-text)" stroke-width="4" fill="none" stroke-linecap="round" stroke-linejoin="round"/>
      </svg>
    </div>
  </div>
  <p class="caption">Check the link in the description<br>to see the animation</p>
</body>
</html>
```